Paper Tides - post rock band album cover design

We are Paper Tides, a post-rock band based on San Jose, CA, USA. We will release a new album “Where the rivers fold" and need a album cover.

The new album is full of emotion and energy. song list:
1. Forward
2. Search (in uploaded files)
3. Before
4. Memory
5. Dream
6. Spring
7. Om Namah Shivaya

Please hear our previous music here
https://paper-tides.soundvault-example.com/album/paper-tides

Target Market(s)

music lovers

Industry/Entity Type

Music Download

Colors

Designer to choose colors to be used in the design.

Requirements
Must have
• album cover + back
• For cover we only need band name (do not need album name), want to use some streamline font for the band name "Paper Tides"
• I attached an example from another band
Nice to have
• I don't want to limit the designers, so please listen to the music and design what you feel the best:)

```html
<!DOCTYPE html>
<html lang="en">
<head>
<meta charset="UTF-8">
<title>Paper Tides — Album Cover</title>
<link rel="stylesheet" href="https://fonts.googleapis.com/css2?family=Herr+Von+Muellerhoff&display=swap">
<style>
  :root {
    --page-bg: #e9e6e1;
    --cover-deep: #2b2833;
    --cover-slate: #3d4552;
    --cover-mist: #6f7c86;
    --cover-glow: #c9d2d6;
    --title-ink: #ffffff;
  }

  html, body {
    margin: 0;
    padding: 0;
    width: 1200px;
    height: 1200px;
    overflow: hidden;
    background: var(--page-bg);
  }

  .album-cover {
    position: relative;
    width: 1200px;
    height: 1200px;
    overflow: hidden;
    background: var(--cover-deep);
  }

  .cover-atmosphere {
    position: absolute;
    inset: 0;
    background:
      radial-gradient(ellipse 38% 30% at 80% 6%, rgba(201, 210, 214, 0.55), rgba(201, 210, 214, 0) 70%),
      radial-gradient(ellipse 55% 45% at 35% 30%, rgba(111, 124, 134, 0.55), rgba(111, 124, 134, 0) 75%),
      radial-gradient(ellipse 50% 40% at 20% 70%, rgba(61, 69, 82, 0.8), rgba(61, 69, 82, 0) 80%),
      linear-gradient(160deg, var(--cover-slate) 0%, #34384a 45%, var(--cover-deep) 100%);
  }

  .band-name {
    position: absolute;
    left: 0;
    right: 0;
    top: 455px;
    margin: 0;
    text-align: center;
    font-family: "Herr Von Muellerhoff", cursive;
    font-weight: 400;
    font-size: 230px;
    line-height: 1;
    color: var(--title-ink);
    letter-spacing: 2px;
    white-space: nowrap;
  }
</style>
</head>
<body>
  <main class="album-cover">
    <div class="cover-atmosphere" role="img" aria-label="Dark smoky haze with soft beams of light falling from the upper right"></div>
    <h1 class="band-name">Paper Tides</h1>
  </main>
</body>
</html>
```